BRL Capital Campaign PWRPT Design

Our school is going to do a fund-raising campaign. I want to design a pwrpt around the campaign and need a design template using some of the images and the content I have laid out.

```html
<!DOCTYPE html>
<html lang="en">
<head>
<meta charset="utf-8">
<title>BRL Capital Campaign Presentation Template</title>
<link href="https://fonts.googleapis.com/css2?family=Montserrat:wght@300;400;500;600;700;800&family=Roboto+Condensed:wght@300;400;700&display=swap" rel="stylesheet">
<style>
  :root{
    --orange:#f68b43;
    --coral:#f96a4b;
    --salmon:#f7845f;
    --yellow:#f6c33c;
    --grass:#2f7a2c;
    --grass-dark:#1f5a1e;
    --slate:#4c5a5a;
    --panel:#eceeee;
    --ink:#2b2b2b;
    --purple:#5a2a7e;
    --white:#ffffff;
  }
  *{box-sizing:border-box;margin:0;padding:0}
  html,body{width:1200px;height:1200px;overflow:hidden;background:var(--white)}
  body{position:relative;font-family:"Montserrat",sans-serif;color:var(--white)}
  .slide{position:absolute;overflow:hidden}
  .copyright-bar{position:absolute;left:0;right:0;bottom:0;height:12px;background:var(--slate);font-size:6px;line-height:12px;padding-left:5px;color:#d9dede;font-family:"Montserrat",sans-serif}
  .brand{position:absolute;display:flex;align-items:center;gap:4px;font-family:"Montserrat",sans-serif;font-weight:300;color:#6a6a6a}
  .brand .mark{width:11px;height:11px;background:var(--orange)}
  .photo{position:absolute}

  /* Title slide */
  .slide--cover{left:250px;top:24px;width:700px;height:394px}
  .slide--cover .photo{inset:0;background:linear-gradient(180deg,#7fb05a 0%,#9cbf7a 35%,#8a8f92 60%,#5f6468 100%)}
  .cover-card{position:absolute;right:14px;bottom:42px;width:212px;height:138px;background:rgba(255,255,255,.94);padding:16px 14px}
  .cover-card .brand{position:static;font-size:34px;color:#3d3d3d}
  .cover-card .brand .mark{width:24px;height:24px}
  .cover-kicker{margin-top:14px;font-family:"Roboto Condensed",sans-serif;font-weight:300;font-size:15px;color:#333}
  .cover-title{margin-top:2px;font-family:"Roboto Condensed",sans-serif;font-weight:700;font-size:19px;color:#222}
  .slide--cover .copyright-bar{height:22px;line-height:22px;font-size:7px;background:#3f4646}

  /* Phase 2 */
  .slide--phase2{left:30px;top:448px;width:560px;height:315px}
  .slide--phase2 .photo{inset:0;background:linear-gradient(180deg,#b7b9b5 0%,#a9b29c 40%,#7fa262 55%,#a8aba5 75%,#b9bab6 100%)}
  .accent-line{position:absolute;left:18px;top:0;width:210px;height:3px;background:var(--yellow)}
  .slide--phase2 .brand{top:10px;right:12px;font-size:17px}
  .phase-tag{position:absolute;left:0;bottom:28px;width:218px;height:68px;background:var(--salmon);padding:12px 10px;font-weight:800;text-transform:uppercase}
  .phase-tag h2{font-size:20px;font-weight:800;letter-spacing:.3px}
  .phase-tag p{font-size:13px;font-weight:800;margin-top:4px}

  /* Phase 1 */
  .slide--phase1{left:610px;top:448px;width:560px;height:315px;background:linear-gradient(160deg,var(--grass) 0%,#2a6e28 50%,var(--grass-dark) 100%)}
  .phase1-heading{position:absolute;left:22px;top:18px;font-size:21px;font-weight:800;letter-spacing:.5px}
  .school-panel{position:absolute;left:0;top:60px;width:216px;height:192px;background:var(--panel);text-align:center;padding-top:22px;color:var(--ink)}
  .school-name{display:flex;align-items:center;justify-content:center;gap:6px;font-weight:700;font-size:14px;color:var(--purple);text-transform:uppercase;line-height:1.15}
  .school-name .mark{width:12px;height:12px;border-radius:50%;background:var(--purple);flex:none}
  .school-name span{display:block;width:130px;text-align:left}
  .project-title{margin-top:44px;font-size:16px;font-weight:800;line-height:1.5;letter-spacing:.3px}
  .floor-plan{position:absolute;left:230px;top:60px;width:316px;height:192px;background:linear-gradient(90deg,#f5dc87 0%,#f3d98a 60%,#7fd9b3 100%);border:2px solid #dcdcdc}
  .credits{position:absolute;right:26px;bottom:20px;display:flex;align-items:center;gap:14px;font-size:11px}
  .credits strong{font-weight:700;font-size:13px;letter-spacing:1px}

  /* Invest slides */
  .slide--invest{width:560px;height:315px}
  .slide--indebted{left:30px;top:800px}
  .slide--invested{left:610px;top:800px}
  .slide--invest .photo{inset:0}
  .slide--indebted .photo{background:linear-gradient(135deg,#e7e7e5 0%,#c9cfd2 50%,#7c8790 100%)}
  .slide--invested .photo{background:linear-gradient(135deg,#efe9e2 0%,#d9d6dc 50%,#8f8aa6 100%)}
  .invest-stripe{position:absolute;left:0;top:0;width:66%;height:100%;background:var(--yellow);clip-path:polygon(0 0,85% 0,100% 100%,0 100%)}
  .invest-panel{position:absolute;left:0;top:0;width:64%;height:100%;clip-path:polygon(0 0,85% 0,100% 100%,0 100%);padding:12px 0 0 10px}
  .slide--indebted .invest-panel{background:var(--orange)}
  .slide--invested .invest-panel{background:var(--coral)}
  .invest-panel h2{font-size:23px;font-weight:800;line-height:1.15;padding-left:4px}
  .invest-lead{margin-top:16px;font-size:11.5px;font-weight:500;line-height:1.45;width:230px}
  .invest-lead b{font-weight:800}
  .invest-lead--large{font-size:14.5px;margin-top:12px;width:260px}
  .invest-list{list-style:none;margin-top:10px;font-size:9.5px;font-weight:600;line-height:1.6}
  .invest-list li::before{content:"";display:inline-block;width:0;height:0;border-left:4px solid transparent;border-right:4px solid transparent;border-bottom:7px solid var(--white);margin-right:5px}
  .verse{margin-top:14px;font-size:7.8px;line-height:1.55;width:272px}
  .slide--invested .verse{margin-top:12px;width:255px}
  .verse-ref{margin-top:12px;font-size:7.8px}
  .verse-ref a{color:var(--yellow);text-decoration:none;font-weight:600}
  .slide--invest .brand{top:10px;right:12px;font-size:17px}
</style>
</head>
<body>

<section class="slide slide--cover">
  <div class="photo" role="img" aria-label="Photo of smiling schoolchildren in hand-painted shirts with their teacher outside the school"></div>
  <div class="cover-card">
    <div class="brand"><span class="mark"></span>Kindlepath</div>
    <p class="cover-kicker">PARTNER WITH US</p>
    <p class="cover-title">PREPARE OUR FUTURE</p>
  </div>
  <div class="copyright-bar">KindlepathTM Routes2workTM 2018 Trademark Kindlepath, LLC</div>
</section>

<section class="slide slide--phase2">
  <div class="photo" role="img" aria-label="Aerial site plan of the campus master plan with sports fields and buildings"></div>
  <div class="accent-line"></div>
  <div class="brand"><span class="mark"></span>Kindlepath</div>
  <div class="phase-tag">
    <h2>Phase 2</h2>
    <p>Master Plan Building</p>
  </div>
  <div class="copyright-bar">Copyright @Text</div>
</section>

<section class="slide slide--phase1" role="group" aria-label="Phase 1 slide on a grass background">
  <h2 class="phase1-heading">PHASE 1</h2>
  <div class="school-panel">
    <div class="school-name"><i class="mark"></i><span>Brookline Ridge Christian School</span></div>
    <p class="project-title">BRL COURTYARD<br>BUILDING ADDITION</p>
  </div>
  <div class="floor-plan" role="img" aria-label="Floor plan of the building addition with five classrooms, a science lab and restrooms along a central corridor"></div>
  <div class="credits">Architect By : <strong>HALDEN</strong><strong>PRYCE</strong></div>
</section>

<section class="slide slide--invest slide--indebted">
  <div class="photo" role="img" aria-label="Photo of a student smiling at a computer lab workstation"></div>
  <div class="invest-stripe"></div>
  <div class="invest-panel">
    <h2>ARE YOU IN<br>(DEBTED)</h2>
    <p class="invest-lead"><b>Indebted</b> to the belief that  we get to choose the culture for our children.</p>
    <p class="verse">"After all, who is Apollos? Who is Paul? We are only God's servants through whom you believed the Good News. Each of us did the work the Lord gave us. I planted the seed in your hearts, and Apollos watered it, but it was God who made it grow. It's not important who does the planting, or who does the watering. What's important is that God makes the seed grow. The one who plants and the one who waters work together with the same purpose. And both will be rewarded for their own hard work. For we are both God's workers. And you are God's field. You are God's building."</p>
    <p class="verse-ref">2 Corinthians 9:6-8 NLT <a>http://versenotes.org/2co.9.6-8.nlt</a></p>
  </div>
  <div class="brand"><span class="mark"></span>Kindlepath</div>
  <div class="copyright-bar">Copyright @Text</div>
</section>

<section class="slide slide--invest slide--invested">
  <div class="photo" role="img" aria-label="Photo of the school basketball team celebrating in uniform"></div>
  <div class="invest-stripe"></div>
  <div class="invest-panel">
    <h2>ARE YOU IN<br>(VESTED)</h2>
    <p class="invest-lead invest-lead--large"><b>invested</b> in the next generation</p>
    <ul class="invest-list">
      <li>Invest in your child's future</li>
      <li>Invest in the next generation</li>
      <li>Invest in our culture</li>
      <li>Invest in the community</li>
    </ul>
    <p class="verse">"Remember this—a farmer who plants only a few seeds will get a small crop. But the one who plants generously will get a generous crop. You must each decide in your heart how much to give. And don't give reluctantly or in response to pressure. "For God loves a person who gives cheerfully." And God will generously provide all you need. Then you will always have everything you need and plenty left over to share with others."</p>
    <p class="verse-ref">2 Corinthians 9:6-8 NLT <a>http://versenotes.org/2co.9.6-8.nlt</a></p>
  </div>
  <div class="brand"><span class="mark"></span>Kindlepath</div>
  <div class="copyright-bar">Copyright @Text</div>
</section>

</body>
</html>
```